professional business card

A Clean looking business card for a money transfer company. Our company is call Velorix= Transfer + Send = Transcend (next level)
to show professionalism as well as some effects to show digital tech.

1 side to have position, name and address
2 side to have company name and show that we provide money exchange and cross-border money transfer

Target Market(s)

Remittance companies and high net worth individuals

Industry/Entity Type

Finance

Contact Information for Business Card

Name, address, email, title, services- money exchange and cross-border remittance

Requirements
Nice to have
• Digital age feel

```html
<!DOCTYPE html>
<html lang="en">
<head>
<meta charset="utf-8">
<title>Velorix Business Card</title>
<link rel="stylesheet" href="https://fonts.googleapis.com/css2?family=Montserrat:wght@600&family=Open+Sans:wght@400;600&display=swap">
<style>
  :root {
    --navy: #263645;
    --cyan: #6cc8db;
    --white: #ffffff;
    --ink: #1c1c1c;
    --backdrop: #8a8a8a;
  }
  html, body {
    margin: 0;
    padding: 0;
    overflow: hidden;
  }
  .canvas {
    position: relative;
    width: 1200px;
    height: 1200px;
    background: var(--backdrop);
    overflow: hidden;
  }
  .card {
    position: absolute;
    overflow: hidden;
  }
  .card-front {
    left: 240px;
    top: 142px;
    width: 720px;
    height: 420px;
    background: var(--white);
  }
  .card-back {
    left: 228px;
    top: 629px;
    width: 744px;
    height: 433px;
    background: var(--navy);
  }
  .wave {
    position: absolute;
    inset: 0;
    width: 100%;
    height: 100%;
  }
  .brand {
    position: absolute;
    display: flex;
    align-items: center;
    gap: 26px;
  }
  .brand-mark {
    width: 56px;
    height: 56px;
    background: var(--cyan);
    flex: none;
  }
  .brand-name {
    font-family: "Montserrat", sans-serif;
    font-weight: 600;
    font-size: 84px;
    line-height: 1;
    letter-spacing: 1px;
  }
  .card-front .brand {
    left: 56px;
    top: 42px;
  }
  .card-front .brand-name { color: var(--navy); }
  .card-back .brand {
    left: 0;
    right: 0;
    top: 178px;
    justify-content: center;
  }
  .card-back .brand-name { color: var(--white); }
  .person {
    position: absolute;
    right: 36px;
    top: 174px;
    text-align: right;
    font-family: "Open Sans", sans-serif;
  }
  .person-name {
    margin: 0;
    font-weight: 600;
    font-size: 25px;
    line-height: 1.2;
    color: var(--navy);
  }
  .person-title {
    margin: 0;
    font-size: 18px;
    line-height: 1.3;
    color: var(--cyan);
  }
  .address {
    position: absolute;
    right: 30px;
    top: 272px;
    margin: 0;
    text-align: right;
    font-family: "Open Sans", sans-serif;
    font-style: normal;
    font-size: 18px;
    line-height: 23px;
    color: var(--ink);
  }
  .contact-list {
    position: absolute;
    left: 34px;
    top: 280px;
    margin: 0;
    padding: 0;
    list-style: none;
    font-family: "Open Sans", sans-serif;
    font-size: 18px;
    line-height: 23px;
    color: var(--white);
  }
  .contact-list li {
    display: flex;
    align-items: center;
    gap: 14px;
  }
  .contact-icon {
    width: 16px;
    height: 16px;
    flex: none;
    fill: none;
    stroke: var(--cyan);
    stroke-width: 1.6;
  }
</style>
</head>
<body>
<main class="canvas">

  <section class="card card-front" aria-label="Business card front">
    <svg class="wave" viewBox="0 0 600 350" preserveAspectRatio="none" aria-hidden="true">
      <path fill="var(--cyan)" d="M0,172 C90,145 220,145 300,205 C360,250 390,300 460,320 C520,336 570,325 600,318 L600,350 L0,350 Z"/>
      <path fill="var(--white)" d="M0,186 C90,160 220,165 290,222 C340,262 360,310 372,350 L0,350 Z"/>
      <path fill="var(--navy)" d="M0,197 C80,170 200,168 265,226 C310,266 335,310 335,350 L0,350 Z"/>
    </svg>

    <div class="brand">
      <span class="brand-mark" aria-hidden="true"></span>
      <span class="brand-name">VELORIX</span>
    </div>

    <div class="person">
      <p class="person-name">Your Name Here</p>
      <p class="person-title">Managing Director</p>
    </div>

    <address class="address">
      480 Meridian Lane,<br>
      #210 Portland, Oregon<br>
      97204
    </address>

    <ul class="contact-list">
      <li>
        <svg class="contact-icon" viewBox="0 0 16 16" aria-hidden="true"><path d="M3 2 L6 2 L7 5 L5.5 6.5 C6.5 8.5 7.5 9.5 9.5 10.5 L11 9 L14 10 L14 13 C8 14 2 8 3 2 Z"/></svg>
        <span>(415) 620-1938</span>
      </li>
      <li>
        <svg class="contact-icon" viewBox="0 0 16 16" aria-hidden="true"><rect x="4.5" y="1.5" width="7" height="13" rx="1.5"/><line x1="7" y1="12" x2="9" y2="12"/></svg>
        <span>(415) 620-1938</span>
      </li>
      <li>
        <svg class="contact-icon" viewBox="0 0 16 16" aria-hidden="true"><rect x="1.5" y="3.5" width="13" height="9"/><path d="M1.5 3.5 L8 9 L14.5 3.5"/></svg>
        <span>youremail@youremail.com</span>
      </li>
      <li>
        <svg class="contact-icon" viewBox="0 0 16 16" aria-hidden="true"><circle cx="8" cy="8" r="6.5"/><ellipse cx="8" cy="8" rx="3" ry="6.5"/><line x1="1.5" y1="8" x2="14.5" y2="8"/></svg>
        <span>www.yourwebsite.com</span>
      </li>
    </ul>
  </section>

  <section class="card card-back" aria-label="Business card back">
    <div class="brand">
      <span class="brand-mark" aria-hidden="true"></span>
      <span class="brand-name">VELORIX</span>
    </div>
  </section>

</main>
</body>
</html>
```